Professional modern business card design

A business card for my nutrition business, wanting a professional look, with info clearly visible. Open to using logo colours too.

Would like key info on the front -
logo
my name and qualifications
email
phone number

and just an enlarged logo again / image on the back.

```html
<!DOCTYPE html>
<html lang="en">
<head>
<meta charset="utf-8">
<title>Verda Nutrition – Business Card</title>
<link rel="stylesheet" href="https://fonts.googleapis.com/css2?family=Open+Sans:wght@700&family=Marcellus&display=swap">
<style>
  :root {
    --bg: #e9e8e5;
    --card: #ffffff;
    --card-shade: #f1f1f1;
    --navy: #0f2a40;
    --lime: #c4d42a;
    --ink: #3d3d3d;
    --sketch: #dfe3e6;
    --sketch-soft: #f3f4f5;
  }
  * { box-sizing: border-box; margin: 0; padding: 0; }
  html, body { width: 1200px; height: 900px; overflow: hidden; }
  body {
    background: var(--bg);
    position: relative;
    font-family: "Marcellus", Georgia, serif;
    color: var(--ink);
  }
  .card {
    position: absolute;
    left: 320px;
    width: 560px;
    height: 320px;
    border-radius: 28px;
    background: linear-gradient(135deg, var(--card) 40%, var(--card-shade));
    box-shadow: 0 10px 28px rgba(0,0,0,.18);
    overflow: hidden;
  }
  .card--logo { top: 70px; }
  .card--contact { top: 500px; }

  .produce-art {
    position: absolute;
    background: radial-gradient(ellipse at center, var(--sketch) 0%, var(--sketch-soft) 60%, rgba(255,255,255,0) 100%);
    opacity: .9;
  }
  .card--logo .produce-art--side { left: 0; top: 0; width: 190px; height: 320px; }
  .card--logo .produce-art--bottom { left: 190px; bottom: 0; width: 200px; height: 110px; }
  .card--contact .produce-art--side { right: 0; top: 0; width: 170px; height: 320px; }
  .card--contact .produce-art--top { right: 170px; top: 0; width: 220px; height: 90px; }
  .card--contact .produce-art--bottom { right: 150px; bottom: 0; width: 140px; height: 150px; }

  .brand {
    position: absolute;
    display: flex;
    align-items: stretch;
    gap: 16px;
  }
  .brand__rule { width: 3px; background: var(--navy); }
  .brand__name {
    font-family: "Open Sans", Arial, sans-serif;
    font-weight: 700;
    color: var(--navy);
    line-height: 1.05;
    display: flex;
    flex-direction: column;
    justify-content: center;
  }
  .card--logo .brand { left: 200px; top: 92px; height: 136px; }
  .card--logo .brand__name { font-size: 50px; }
  .card--contact .brand { left: 34px; top: 196px; height: 110px; }
  .card--contact .brand__name { font-size: 40px; }

  .contact { position: absolute; left: 40px; top: 36px; }
  .contact__name { color: var(--lime); font-size: 17px; letter-spacing: .06em; text-transform: uppercase; }
  .contact__role { font-size: 16px; margin-top: 2px; }
  .contact__list { list-style: none; margin-top: 22px; font-size: 16px; }
  .contact__list li { display: flex; align-items: center; gap: 10px; margin-bottom: 6px; }
  .contact__list svg { width: 14px; height: 14px; fill: none; stroke: var(--navy); stroke-width: 1.6; }
  .divider {
    position: absolute;
    left: 0; top: 176px;
    width: 330px; height: 1.5px;
    background: var(--lime);
  }
</style>
</head>
<body>
  <section class="card card--logo" aria-label="Logo side">
    <div class="produce-art produce-art--side" role="img" aria-label="Light line sketches of vegetables and herbs"></div>
    <div class="produce-art produce-art--bottom" role="img" aria-label="Light line sketches of tomatoes, banana and dill"></div>
    <div class="brand">
      <span class="brand__rule"></span>
      <span class="brand__name"><span>Verda</span><span>Nutrition</span></span>
    </div>
  </section>

  <section class="card card--contact" aria-label="Contact side">
    <div class="produce-art produce-art--top" role="img" aria-label="Light line sketches of avocado, leek and mushroom"></div>
    <div class="produce-art produce-art--side" role="img" aria-label="Light line sketches of herbs, ginger and peppers"></div>
    <div class="produce-art produce-art--bottom" role="img" aria-label="Light line sketches of tomatoes and banana"></div>
    <div class="contact">
      <p class="contact__name">Mara Ellison</p>
      <p class="contact__role">Director</p>
      <ul class="contact__list">
        <li><svg viewBox="0 0 14 14"><rect x="3.5" y="1" width="7" height="12" rx="1.2"/><line x1="6" y1="11" x2="8" y2="11"/></svg>555-214-0387</li>
        <li><svg viewBox="0 0 14 14"><rect x="1" y="3" width="12" height="8.5" rx="1"/><polyline points="1,3.5 7,8 13,3.5"/></svg>mara@verdanutrition.com</li>
      </ul>
    </div>
    <span class="divider"></span>
    <div class="brand">
      <span class="brand__rule"></span>
      <span class="brand__name"><span>Verda</span><span>Nutrition</span></span>
    </div>
  </section>
</body>
</html>
```